New Wordpress theme/Update website

Many of our plug ins are in need to updating and Id like to make my website more modern. We are a Chiropractic office and our logo colors are black, white and red. My goal is to have an updated look that allows me to make simple edits(such as i currently have limitations on # of employee profiles) and stay operating well on my corvexhost hosting compnay ive prepaid for a few years for. And to keep working well on the mobile platform. Can email all the edits id like to make to www.DrMarcusHalvern.com Thanks
Here are the exact edits:
bright red, colors, etc
Change NEw patient Tab from coupon to special offers-Change word download on NP forms
Remove blog text on sites
UPDATE VIDSTREAMO videos-Upload all from PK-So the VidStreamo link on site is relevant-REmove 2 tabs on top
Update FAQ tab to our recent edited sheet on common myths
Update office hours
Testimonial videos on conditions page -LBP-back pain video, etc. and one landing page or smaller icon on home page but when you click it pops up larger over website.
Keep video on front but put elsewhere. Lower on office tour with pics, but video icon is first.
add MOST INSURANCES ACCEPTED
Add Heal Strong Walk Strong Live Strong
Capitalize We diagnose & address the root cause to your health problem
Eliminate Home Exercise Tab?
Instead of video , picture office tour that rotates-use blur iphone pics
black bright red and white-black and white backgrounds alternate as you scroll down page
New testimonial videos -with Me and DrW-LINKS FOR PATIENT VIDEOS or MY VIDEOS-Educational
Unlimited Staff profiles-easy to change
Scrolling down home page-Pain pic on top, then office team pic then below that office tour, then map
Call to action tabs-Free Consult-Free Mechanical Massage, MASSAGE coupon
Change about us to meet the team?
Single space my bullets -Profile
Merge Location into Contact Us
all conditions on home page on one tab
Pain relief picture? Heal Strong Walk Strong Live Strong tagline-On top wording explains what we do-Root cause. Then 3 clickable buttons below-New patients-Scheduling-Meet the team-Back Brace-Vitamins?
update layout, pictures(thoroughout), coloring, and flow of the main page
about us page also layout wayyyyyyyyyy to wordy
services pages again layout and wordy, bulleted points not necessary when listing services
personally interesting facts adn stas are not needed and articles ( if that stuff was important to you ass links for them)
FAQ is its own tab why is it also under services ? one place only (layout on this page)
weightloss tab isnt even avalible...page not found
is Norvale Imaging and Spinal Review a necessary tab ?
for the supplements it has no details, simply directs you to nutrovance page ( not in a new tab either )which I feel can be confusing. We use their products but its listed under services. what are those services in regards to supplements, know what I mean?
for location the plotmap map is unable to load map correctly......not helpful. also why is the description of what we do within the directions on how to find us? and when clicking the lionk for directions this message pops up 'There was an error geocoding your location. Check the address and try again"
video testimonals need major updating
also on blog/news you have misconceptions abouit chiro, redundant, these type of things should be on the FAQ page.
social media tabs, relevance of the first and last button
Also their supplement tab leads to our own page...explains to picks then a link for separate landing page to buy , include velumora that way. And stress support in office.
Go into their practice area tab and a short way down they have what they offer there but it’s in a box that you go left or right to see what they offer. It’s neater and still gets point across
They do this again under conditions. I’d like to see this utilized for our sight :)
Also like you mentioned we had but I couldn’t see. Is at the bottom of each page was a click to schedule appointment that’s 👌🏼 Perfect
https://www.qrtvhealthhub.com/
http://www.zkwnstudio.com/
http://www.brightfieldvitalsupply.com/
Refer to https://tallowmerespine.com/ to see how conditions treated was put in
OR EVOLVING PIC
CODING is already included on thebudget for this website.

```html
<!DOCTYPE html>
<html lang="en">
<head>
<meta charset="utf-8">
<title>Halvern Chiropractic &amp; Wellness Center</title>
<link href="https://fonts.googleapis.com/css2?family=Open+Sans:wght@400;600;700&family=Raleway:wght@300;400;600;700&display=swap" rel="stylesheet">
<style>
:root{
  --red:#e3232c;
  --red-dark:#b8151c;
  --pink:#f7b7bb;
  --ink:#1d1d1d;
  --text:#444;
  --grey-bg:#f1f1f1;
  --footer-bg:#ebebeb;
  --white:#fff;
}
*{margin:0;padding:0;box-sizing:border-box}
html,body{width:1200px;height:5373px;overflow:hidden;background:var(--white)}
body{position:relative;font-family:"Open Sans",Arial,sans-serif;color:var(--text)}
.abs{position:absolute}
.heading{font-family:"Raleway",Arial,sans-serif;font-weight:300;color:var(--ink);text-align:center;width:1200px;left:0}
.divider{display:block;margin:10px auto 0}

/* header */
.topbar{top:0;left:0;width:1200px;height:90px;background:var(--white)}
.brand{left:92px;top:24px;display:flex;align-items:center;gap:10px;font-family:"Open Sans",sans-serif;font-weight:700;font-size:27px;color:var(--ink)}
.brand-dot{width:34px;height:34px;border-radius:50%;border:3px solid var(--red)}
.phone{left:710px;top:27px;display:flex;align-items:center;gap:14px;font-weight:700;font-size:17px;color:var(--ink)}
.phone-icon{width:36px;height:36px;border-radius:50%;background:var(--red);display:flex;align-items:center;justify-content:center}
.social-mini{left:958px;top:36px;display:flex;gap:22px}
.social-mini span{width:14px;height:14px;border-radius:50%;background:#9a9a9a}
.nav{top:90px;left:0;width:1200px;height:43px;background:var(--red);display:flex;align-items:center;padding-left:95px;gap:40px}
.nav a{color:var(--white);text-decoration:none;font-size:15px;font-weight:600}

/* hero */
.hero{top:133px;left:0;width:1200px;height:560px;background:linear-gradient(90deg,#f3f1ef 0%,#eae4df 35%,#d9c7bb 60%,#c9a993 100%)}
.hero-title{left:88px;top:55px;font-family:"Raleway",sans-serif;font-weight:300;font-size:62px;line-height:1.05;color:var(--ink)}
.hero-tag{left:192px;top:195px;font-family:"Raleway",sans-serif;font-weight:400;font-size:22px;color:var(--red)}
.hero-dots{left:545px;top:488px;display:flex;gap:16px}
.hero-dots span{width:13px;height:13px;border-radius:50%;background:var(--white)}
.hero-dots span:first-child{background:var(--red)}
.hero-wave{left:0;top:470px}

/* treatment circles */
.tcircle{border-radius:50%;border:12px solid var(--red);overflow:hidden;box-shadow:0 6px 18px rgba(0,0,0,.25)}
.tcircle .photo{width:100%;height:100%}
.tcircle .label{position:absolute;left:0;right:0;background:rgba(20,20,20,.88);color:var(--white);font-weight:700;text-align:center}

/* red welcome band */
.welcome{top:1325px;left:0;width:1200px;height:465px;background:linear-gradient(180deg,#d7242b 0%,#c61c23 60%,#b8171e 100%)}
.welcome h2{font-family:"Raleway",sans-serif;font-weight:300;font-size:40px;color:var(--white);text-align:center;margin-top:88px}
.welcome p{width:820px;margin:28px auto 0;text-align:center;color:#fde5e6;font-size:14.5px;line-height:2}

/* treatment list */
.treat-list{top:2010px;left:190px;width:900px;display:grid;grid-template-columns:325px 322px 250px;row-gap:26px}
.treat-list li{list-style:none;position:relative;padding-left:34px;font-size:18px;color:var(--ink);line-height:1.25}
.treat-list li::before{content:"";position:absolute;left:2px;top:4px;border-left:12px solid var(--red);border-top:8px solid transparent;border-bottom:8px solid transparent}

/* services */
.services{top:2418px;left:0;width:1200px;height:645px;background:var(--grey-bg)}
.svc{width:316px;height:316px;border-radius:50%;overflow:hidden;border:6px solid var(--white);box-shadow:0 4px 12px rgba(0,0,0,.15)}
.svc .photo{height:65%}
.svc .band{height:35%;color:var(--white);text-align:center;font-family:"Raleway",sans-serif;font-size:30px;padding-top:12px}
.svc .band.red{background:var(--red)}
.svc .band.dark{background:#2a2a2a}
.arrow{top:2775px}

/* testimonials */
.video{width:322px;height:219px}
.play{position:absolute;left:50%;top:50%;transform:translate(-50%,-50%)}
.dots{top:3558px;left:565px;display:flex;gap:10px}
.dots span{width:13px;height:13px;border-radius:50%;border:2px solid #888}
.dots span:first-child{background:#888}

/* contact */
.contact-bg{top:3654px;left:0;width:1200px;height:823px;background:linear-gradient(90deg,#6e5140 0%,#9b7a5f 30%,#d8cbbd 60%,#efe9e3 100%)}
.contact-card{top:3826px;left:387px;width:483px;height:456px;background:#141414;padding:38px 40px}
.contact-card h2{color:var(--white);font-family:"Open Sans",sans-serif;font-weight:700;font-size:40px;text-align:center;margin-bottom:26px}
.field{background:var(--white);height:40px;margin-bottom:10px;font-size:13px;color:#333;padding:10px 12px}
.field.tall{height:95px}
.book{display:block;margin:26px auto 0;width:140px;height:46px;border-radius:23px;background:var(--red);color:var(--white);font-weight:700;font-size:14px;text-align:center;line-height:46px}

/* newsletter */
.news-text{top:4643px;left:320px;width:560px;text-align:center;font-size:13px;line-height:1.9;color:#666}
.news-form{top:4736px;left:315px;width:625px;height:48px;display:flex;border:1px solid #ddd;background:var(--white)}
.news-form .ico{width:48px;background:var(--red);display:flex;align-items:center;justify-content:center}
.news-form .input{flex:1;padding:15px 16px;font-size:13px;color:#999}
.news-form .btn{width:145px;background:var(--red);color:var(--white);font-weight:700;font-size:14px;text-align:center;line-height:48px}
.social{top:4825px;left:505px;display:flex;gap:14px}
.social span{width:34px;height:34px;border-radius:50%}

/* footer */
.footer{top:4979px;left:0;width:1200px;height:394px;background:var(--footer-bg)}
.fcol{width:300px;text-align:center;font-size:13px;line-height:1.9;color:#555}
.fcol h3{font-family:"Raleway",sans-serif;font-weight:500;font-size:22px;color:var(--ink);margin-bottom:22px}
.copy{top:5322px;left:0;width:1200px;text-align:center;font-size:11px;color:#555}
</style>
</head>
<body>

<header>
  <div class="abs topbar"></div>
  <div class="abs brand"><span class="brand-dot"></span>Halvern Chiropractic &amp; Wellness Center</div>
  <div class="abs phone">
    <span class="phone-icon"><svg width="18" height="18" viewBox="0 0 24 24"><path fill="#fff" d="M6.6 10.8a15 15 0 0 0 6.6 6.6l2.2-2.2c.3-.3.7-.4 1-.2 1.1.4 2.3.6 3.6.6.6 0 1 .4 1 1V20c0 .6-.4 1-1 1A17 17 0 0 1 3 4c0-.6.4-1 1-1h3.5c.6 0 1 .4 1 1 0 1.3.2 2.5.6 3.6.1.3 0 .7-.2 1z"/></svg></span>
    215 480 3921
  </div>
  <div class="abs social-mini"><span></span><span></span><span></span><span></span></div>
  <nav class="abs nav">
    <a>Home</a><a>About Us</a><a>Services</a><a>New Patients</a><a>Faq</a><a>Home Exercises</a><a>Location</a><a>Blog / News</a><a>Contact</a>
  </nav>
</header>

<section class="abs hero" role="img" aria-label="Woman relaxing as a chiropractor's hands rest on her head">
  <h1 class="abs hero-title">Halvern Chiropractic &amp;<br>Wellness Center</h1>
  <p class="abs hero-tag">Heal strong, walk strong, and live strong!</p>
  <div class="abs hero-dots"><span></span><span></span><span></span><span></span></div>
  <svg class="abs hero-wave" width="1200" height="95" viewBox="0 0 1200 95">
    <path d="M0 30 Q300 95 600 60 T1200 20 V95 H0Z" fill="var(--pink)"/>
    <path d="M0 55 Q300 110 620 78 T1200 50 V95 H0Z" fill="#fff"/>
  </svg>
</section>

<section class="treatments">
  <div class="abs tcircle" style="left:190px;top:895px;width:262px;height:262px">
    <div class="photo" role="img" aria-label="Man holding his head with a headache" style="background:linear-gradient(160deg,#cfc9c4,#8c847e)"></div>
    <div class="label" style="top:140px;height:48px;line-height:48px;font-size:17px">Headache Treatment</div>
  </div>
  <div class="abs tcircle" style="left:760px;top:895px;width:262px;height:262px">
    <div class="photo" role="img" aria-label="Woman holding her neck in pain" style="background:linear-gradient(160deg,#e2d3c7,#a8877a)"></div>
    <div class="label" style="top:125px;height:70px;padding-top:10px;font-size:16px;line-height:1.4">Neck and Back<br>Pain Treatment</div>
  </div>
  <div class="abs tcircle" style="left:420px;top:845px;width:360px;height:360px;border-width:16px">
    <div class="photo" role="img" aria-label="Person holding a sore knee" style="background:linear-gradient(160deg,#e9d9cd,#b58d76)"></div>
    <div class="label" style="top:190px;height:86px;padding-top:14px;font-size:21px;line-height:1.4">Arm and Leg Pain<br>Treatment</div>
  </div>
</section>

<section class="abs welcome" role="img" aria-label="Clinic interior under a red tint">
  <h2>Heal strong, walk strong, and live strong!</h2>
  <svg class="divider" width="80" height="8" viewBox="0 0 80 8"><polyline points="0,4 10,1 20,7 30,1 40,7 50,1 60,7 70,1 80,4" fill="none" stroke="#fff" stroke-width="2"/></svg>
  <p>Welcome to Halvern Chiropractic Center in Ashbury, Norvale County, PA. To optimize your health, we tailor make a customized treatment plan for you by addressing your physical, chemical and emotional stress. No matter what your injury may be, our unique approach to treating the root cause of your health problems may provide wellness solutions you have not yet tried. To help you improve your quality of life and achieve your goals we offer chiropractic care, massage therapy, physiotherapy modalities, weight loss, exercise, lifestyle management, nutraceutical grade supplements and x-ray imaging under one roof.</p>
</section>

<section class="conditions">
  <h2 class="abs heading" style="top:1890px;font-size:40px">We offer treatment for all of the following</h2>
  <svg class="abs" style="left:560px;top:1950px" width="80" height="8" viewBox="0 0 80 8"><polyline points="0,4 10,1 20,7 30,1 40,7 50,1 60,7 70,1 80,4" fill="none" stroke="var(--red)" stroke-width="2"/></svg>
  <ul class="abs treat-list">
    <li>Back Problems</li><li>Migraines</li><li>Shoulder Pain</li>
    <li>Body Fat Reduction</li><li>Neck Pain</li><li>Spinal Problem</li>
    <li>Disc Problems</li><li>Pinched Nerve</li><li>Sports Injuries</li>
    <li>Headaches</li><li>Sciatica</li><li>Upper Back Pain</li>
    <li>Herniated Disc Injury</li><li>Scoliosis Correction</li><li>Whiplash</li>
    <li>Lower Back Pain</li><li>Muscle Aches, Sprains and Strains</li><li>Hip, Knee, Ankle, &amp; Foot Problems</li>
  </ul>
</section>

<section class="abs services">
  <h2 class="abs heading" style="top:108px;font-size:40px">Our Services</h2>
  <svg class="abs" style="left:560px;top:166px" width="80" height="8" viewBox="0 0 80 8"><polyline points="0,4 10,1 20,7 30,1 40,7 50,1 60,7 70,1 80,4" fill="none" stroke="var(--red)" stroke-width="2"/></svg>
</section>
<div class="abs svc" style="left:107px;top:2643px">
  <div class="photo" role="img" aria-label="Woman doing a yoga stretch" style="background:linear-gradient(180deg,#e4e9e2,#b9c4b4)"></div>
  <div class="band red">Exercise<br><svg width="14" height="12" viewBox="0 0 14 12"><polyline points="2,2 7,6 12,2" fill="none" stroke="#fff" stroke-width="2"/><polyline points="2,6 7,10 12,6" fill="none" stroke="#fff" stroke-width="2"/></svg></div>
</div>
<div class="abs svc" style="left:442px;top:2643px">
  <div class="photo" role="img" aria-label="Person receiving a back massage" style="background:linear-gradient(180deg,#efe2d3,#c99e7d)"></div>
  <div class="band dark">Massage<br><svg width="14" height="12" viewBox="0 0 14 12"><polyline points="2,2 7,6 12,2" fill="none" stroke="#fff" stroke-width="2"/><polyline points="2,6 7,10 12,6" fill="none" stroke="#fff" stroke-width="2"/></svg></div>
</div>
<div class="abs svc" style="left:776px;top:2643px">
  <div class="photo" role="img" aria-label="Therapist working on a patient's shoulder" style="background:linear-gradient(180deg,#e3e6ea,#9ea7b2)"></div>
  <div class="band red">Physiotherapy<br><svg width="14" height="12" viewBox="0 0 14 12"><polyline points="2,2 7,6 12,2" fill="none" stroke="#fff" stroke-width="2"/><polyline points="2,6 7,10 12,6" fill="none" stroke="#fff" stroke-width="2"/></svg></div>
</div>
<svg class="abs arrow" style="left:36px" width="16" height="26" viewBox="0 0 16 26"><polyline points="13,2 3,13 13,24" fill="none" stroke="#555" stroke-width="3"/></svg>
<svg class="abs arrow" style="left:1148px" width="16" height="26" viewBox="0 0 16 26"><polyline points="3,2 13,13 3,24" fill="none" stroke="#555" stroke-width="3"/></svg>

<section class="testimonials">
  <h2 class="abs heading" style="top:3168px;font-size:40px">Testimonials</h2>
  <svg class="abs" style="left:560px;top:3226px" width="80" height="8" viewBox="0 0 80 8"><polyline points="0,4 10,1 20,7 30,1 40,7 50,1 60,7 70,1 80,4" fill="none" stroke="var(--red)" stroke-width="2"/></svg>
  <div class="abs video" style="left:90px;top:3281px;background:linear-gradient(135deg,#7b6e63,#3c3530)" role="img" aria-label="Video still of a patient testimonial">
    <svg class="play" width="60" height="60" viewBox="0 0 60 60"><circle cx="30" cy="30" r="27" fill="rgba(0,0,0,.55)" stroke="#fff" stroke-width="3"/><polygon points="24,18 42,30 24,42" fill="#fff"/></svg>
  </div>
  <div class="abs video" style="left:440px;top:3281px;background:linear-gradient(135deg,#8a7a6c,#4b3f37)" role="img" aria-label="Video still of a patient testimonial">
    <svg class="play" width="60" height="60" viewBox="0 0 60 60"><circle cx="30" cy="30" r="27" fill="rgba(0,0,0,.55)" stroke="#fff" stroke-width="3"/><polygon points="24,18 42,30 24,42" fill="#fff"/></svg>
  </div>
  <div class="abs video" style="left:788px;top:3281px;background:linear-gradient(135deg,#8c8f93,#4a4c50)" role="img" aria-label="Video still of a patient testimonial">
    <svg class="play" width="60" height="60" viewBox="0 0 60 60"><circle cx="30" cy="30" r="27" fill="rgba(0,0,0,.55)" stroke="#fff" stroke-width="3"/><polygon points="24,18 42,30 24,42" fill="#fff"/></svg>
  </div>
  <div class="abs dots"><span></span><span></span><span></span></div>
</section>

<section class="abs contact-bg" role="img" aria-label="Woman holding a yoga pose in a wooden studio">
  <svg class="abs" style="left:0;top:-1px" width="1200" height="110" viewBox="0 0 1200 110"><path d="M0 0 H1200 V40 Q900 -10 600 50 T0 40Z" fill="#fff"/></svg>
  <svg class="abs" style="left:0;top:700px" width="1200" height="124" viewBox="0 0 1200 124"><path d="M0 60 Q300 0 650 60 T1200 40 V124 H0Z" fill="var(--pink)"/><path d="M0 85 Q300 30 650 85 T1200 65 V124 H0Z" fill="#fff"/></svg>
</section>
<form class="abs contact-card">
  <h2>Contact Us</h2>
  <div class="field">Name</div>
  <div class="field">Email</div>
  <div class="field">Phone</div>
  <div class="field tall">Message</div>
  <div class="book">BOOK NOW</div>
</form>

<section class="newsletter">
  <h2 class="abs heading" style="top:4572px;font-size:42px;font-weight:400">Subscribe Our Newsletter</h2>
  <p class="abs news-text">Join our mailing list for seasonal health tips, clinic news and special offers sent straight to your inbox each month, free of charge.</p>
  <div class="abs news-form">
    <span class="ico"><svg width="20" height="14" viewBox="0 0 20 14"><rect x="1" y="1" width="18" height="12" fill="none" stroke="#fff" stroke-width="2"/><polyline points="1,1 10,8 19,1" fill="none" stroke="#fff" stroke-width="2"/></svg></span>
    <span class="input">Enter Your Email Address</span>
    <span class="btn">SUBSCRIBE</span>
  </div>
  <div class="abs social">
    <span style="background:#3b5a9a"></span><span style="background:#29a9e1"></span><span style="background:#f3a21b"></span><span style="background:#d9232d"></span><span style="background:#1b86b7"></span>
  </div>
</section>

<footer class="abs footer">
  <div class="abs fcol" style="left:72px;top:78px">
    <h3>ABOUT US</h3>
    <p>Caring for our community with gentle,<br>hands-on chiropractic care that helps<br>every patient move and feel better.</p>
  </div>
  <div class="abs fcol" style="left:450px;top:68px">
    <h3>OPEN HOURS</h3>
    <p>Mon-Fri: 9 AM – 6 PM<br>Saturday: 9 AM – 12 PM<br>Sunday: Closed</p>
  </div>
  <div class="abs fcol" style="left:835px;top:68px">
    <h3>CONTACT</h3>
    <p>118 Ferncrest Ave. Ste 4 Ashbury,<br>Pennsylvania 19208<br>Email: <span style="color:var(--red)">info@halvernwellness.com</span><br>Telephone: 215-480-3921</p>
  </div>
  <p class="abs copy" style="top:343px">© Copyrights 2018 The Company name All Rights Reserved</p>
</footer>

</body>
</html>
```